Hi,

I have just started up a business called VELUMO in Melbourne. We run fun street art tours around Melbourne's CBD.

I need to create a design for the back side of my business cards. I have designed the front side (simply with my logo) however, I am having trouble designing the reverse side in a professional manner. I have attached pictures of what I have done.

The picture attached titled "VELUMO Business Cards Back" has all the information that I require on the back side of my business cards; although displayed in an amateur and simple way. As displayed in the picture, I need: the VELUMO logo, the website URL, the booking details (phone - 0481 556 217 & email - bookings@velumo.com.au) and the service description ($20, One Hour, Tours Daily, Meet at Carrow Rd Terminal). I would also like to use the font in the picture supplied which is "source-sans-pro".

The VELUMO tours are for tourists and are relaxed, entertaining and fun! I would like the design to reflect this.

Target Market(s)

Backpackers & University Students

Industry/Entity Type

Business

Requirements
Must have
• The VELUMO logo, the website URL, the booking details (phone - 0481 556 217 & email - bookings@velumo.com.au) and the service description ($20, One Hour, Tours Daily, Meet at Carrow Rd Terminal).

```html
<!DOCTYPE html>
<html lang="en">
<head>
<meta charset="utf-8">
<title>VELUMO Business Cards</title>
<link href="https://fonts.googleapis.com/css2?family=Source+Sans+3:wght@300;400;600;700&display=swap" rel="stylesheet">
<style>
  :root {
    --page: #ffffff;
    --wall-light: #dde9ea;
    --wall-mid: #c9dadc;
    --wall-shadow: #b9cbcd;
    --rust: #c9843f;
    --rust-soft: #d9ab78;
    --ink: #222222;
    --ink-light: #3a3a3a;
    --accent: #e85a50;
  }
  html, body {
    margin: 0;
    padding: 0;
    width: 1200px;
    height: 1000px;
    overflow: hidden;
    background: var(--page);
    font-family: "Source Sans 3", sans-serif;
    color: var(--ink);
  }
  .canvas {
    position: relative;
    width: 1200px;
    height: 1000px;
  }
  .card {
    position: absolute;
    left: 242px;
    width: 715px;
    height: 397px;
    overflow: hidden;
  }
  .card--front { top: 83px; }
  .card--back { top: 520px; }

  .wall {
    position: absolute;
    inset: 0;
  }
  .card--front .wall {
    background:
      radial-gradient(ellipse 320px 120px at 600px 20px, var(--rust) 0%, var(--rust-soft) 45%, rgba(217,171,120,0) 100%),
      radial-gradient(ellipse 500px 300px at 30% 70%, var(--wall-light), var(--wall-mid) 100%);
  }
  .card--back .wall {
    background: radial-gradient(ellipse 520px 320px at 45% 45%, var(--wall-light), var(--wall-mid) 80%, var(--wall-shadow) 100%);
  }

  .brand {
    position: absolute;
    margin: 0;
    font-weight: 700;
    color: var(--accent);
    letter-spacing: 2px;
    line-height: 1;
  }
  .card--front .brand {
    left: 0;
    right: 0;
    top: 134px;
    text-align: center;
    font-size: 60px;
    padding-left: 26px;
  }
  .card--back .brand {
    left: 400px;
    top: 70px;
    width: 260px;
    text-align: center;
    font-size: 50px;
  }

  .tagline {
    position: absolute;
    left: 0;
    right: 0;
    top: 233px;
    margin: 0;
    padding-left: 26px;
    text-align: center;
    font-size: 29px;
    font-weight: 600;
    line-height: 39px;
    color: var(--ink);
  }

  .details {
    position: absolute;
    left: 71px;
    top: 63px;
    margin: 0;
    padding: 0;
    list-style: none;
    font-size: 25px;
    line-height: 33.5px;
  }
  .details__label {
    font-weight: 300;
    color: var(--ink-light);
  }
  .details__value { font-weight: 400; }

  .booking {
    position: absolute;
    left: 71px;
    top: 231px;
    margin: 0;
    font-size: 25px;
    font-weight: 700;
    line-height: 33.5px;
  }
  .booking span { display: block; }

  .website {
    position: absolute;
    left: 423px;
    top: 298px;
    margin: 0;
    font-size: 25px;
    font-weight: 300;
    color: var(--accent);
    line-height: 33.5px;
  }
</style>
</head>
<body>
<main class="canvas">
  <section class="card card--front" aria-label="Business card front">
    <div class="wall" role="img" aria-label="Weathered pale blue concrete wall with rusty orange patch"></div>
    <h1 class="brand">VELUMO</h1>
    <p class="tagline">Melbourne Street Art<br>Walking Tours</p>
  </section>

  <section class="card card--back" aria-label="Business card back">
    <div class="wall" role="img" aria-label="Weathered pale blue concrete wall texture"></div>
    <h2 class="brand">VELUMO</h2>
    <ul class="details">
      <li><span class="details__label">Price?</span> <span class="details__value">$20</span></li>
      <li><span class="details__label">How long?</span> <span class="details__value">One Hour</span></li>
      <li><span class="details__label">When?</span> <span class="details__value">Daily Tours</span></li>
      <li><span class="details__label">Where?</span> <span class="details__value">Meet at Carrow Rd Terminal</span></li>
    </ul>
    <p class="booking">
      <span>Call Jax to BOOK NOW!</span>
      <span>0481 556 217</span>
      <span>bookings@velumo.com.au</span>
    </p>
    <p class="website">www.velumo.com.au</p>
  </section>
</main>
</body>
</html>
```